A Maverick Business Card for a Maverick Company!

We're a maverick, 'rule breaker' market research company that needs a maverick business card design to suit who we are!

All logos, colours and text are detailed in the attached briefing document.

Note Please ignore the 'Look & Feel' wizard results and refer ONLY to the attached brief.

```html
<!DOCTYPE html>
<html lang="en">
<head>
<meta charset="utf-8">
<title>Northlens Research – Business Card</title>
<link rel="stylesheet" href="https://fonts.googleapis.com/css2?family=Barlow:wght@400;500;600&display=swap">
<style>
  :root {
    --backdrop: #e6e7e8;
    --card-white: #ffffff;
    --brand-red: #e41e26;
    --brand-red-deep: #b5141b;
    --band-red: #a80f16;
    --ink: #2b2b2b;
    --ink-soft: #6b6b6b;
    --ink-strip: #333333;
  }
  * { margin: 0; padding: 0; box-sizing: border-box; }
  html, body { width: 1200px; height: 1200px; overflow: hidden; }
  body {
    background: var(--backdrop);
    font-family: "Barlow", Arial, sans-serif;
    position: relative;
  }
  .card {
    position: absolute;
    left: 301px;
    width: 597px;
    overflow: hidden;
  }
  /* Front */
  .card-front {
    top: 215px;
    height: 361px;
    background: var(--card-white);
  }
  .front-wordmark {
    position: absolute;
    left: 43px;
    top: 50px;
    display: flex;
    align-items: center;
    gap: 12px;
    color: var(--brand-red);
    font-weight: 600;
    font-size: 32px;
    letter-spacing: 0.5px;
  }
  .wordmark-dot {
    width: 28px; height: 28px;
    border-radius: 50%;
    background: var(--brand-red);
  }
  .person-name {
    position: absolute;
    left: 43px; top: 190px;
    font-size: 21px; font-weight: 500;
    color: var(--ink);
  }
  .person-role {
    position: absolute;
    left: 43px; top: 217px;
    font-size: 16.5px;
    color: var(--ink-soft);
  }
  .contact-list {
    position: absolute;
    left: 43px; top: 285px;
    font-size: 14.5px;
    line-height: 20px;
    color: var(--ink-soft);
    list-style: none;
  }
  .contact-label { color: var(--brand-red); font-weight: 500; }
  .contact-gap { margin-left: 8px; }

  /* Back */
  .card-back {
    top: 624px;
    height: 363px;
    background: linear-gradient(180deg, var(--brand-red) 0%, var(--brand-red-deep) 100%);
    color: var(--card-white);
  }
  .back-panel {
    position: absolute;
    left: 0; top: 0; width: 100%; height: 280px;
  }
  .back-wordmark {
    position: absolute;
    top: 68px; left: 0; width: 100%;
    display: flex; justify-content: center; align-items: center; gap: 14px;
    font-weight: 600; font-size: 38px; letter-spacing: 0.5px;
  }
  .back-wordmark .wordmark-dot { background: var(--card-white); width: 32px; height: 32px; }
  .tagline {
    position: absolute;
    top: 130px; left: 0; width: 100%;
    text-align: center;
    font-size: 14px; line-height: 16px;
  }
  .benefits {
    position: absolute;
    top: 190px; left: 0; width: 100%;
    list-style: none;
    text-align: center;
    font-size: 17px; line-height: 22.5px; font-weight: 500;
  }
  .benefits li { display: flex; justify-content: center; align-items: center; gap: 6px; }
  .tick { width: 14px; height: 12px; }
  .address-strip {
    position: absolute;
    top: 280px; left: 0; width: 100%; height: 32px;
    background: var(--card-white);
    color: var(--ink-strip);
    font-size: 14px;
    display: flex; align-items: center; justify-content: center;
  }
  .web-band {
    position: absolute;
    top: 312px; left: 0; width: 100%; height: 51px;
    background: var(--band-red);
    font-size: 14px;
    display: flex; align-items: center; justify-content: center;
  }
  .web-band strong { font-weight: 600; }
</style>
</head>
<body>

<section class="card card-front" aria-label="Business card front">
  <div class="front-wordmark"><span class="wordmark-dot"></span>Northlens Research</div>
  <p class="person-name">Dean Whitmore</p>
  <p class="person-role">Managing Director</p>
  <ul class="contact-list">
    <li><span class="contact-label">Phone</span> 1300 555 214 <span class="contact-label contact-gap">Direct</span> 0400 555 382</li>
    <li><span class="contact-label">Fax</span> 03 9555 0187 <span class="contact-label contact-gap">Email</span> dean@northlensresearch.com.au</li>
  </ul>
</section>

<section class="card card-back" aria-label="Business card back">
  <div class="back-panel">
    <div class="back-wordmark"><span class="wordmark-dot"></span>Northlens Research</div>
    <p class="tagline">Sharp, honest research that skips<br>the big agency overheads</p>
    <ul class="benefits">
      <li><svg class="tick" viewBox="0 0 14 12" aria-hidden="true"><path d="M1 6.5 L5 10.5 L13 1.5" fill="none" stroke="#fff" stroke-width="2.6" stroke-linecap="round" stroke-linejoin="round"/></svg>Professional market research – tailored, inexpensive and fast</li>
      <li><svg class="tick" viewBox="0 0 14 12" aria-hidden="true"><path d="M1 6.5 L5 10.5 L13 1.5" fill="none" stroke="#fff" stroke-width="2.6" stroke-linecap="round" stroke-linejoin="round"/></svg>Take a data-centric approach to your decision-making</li>
      <li><svg class="tick" viewBox="0 0 14 12" aria-hidden="true"><path d="M1 6.5 L5 10.5 L13 1.5" fill="none" stroke="#fff" stroke-width="2.6" stroke-linecap="round" stroke-linejoin="round"/></svg>Submit an online research brief and we will do the rest</li>
    </ul>
  </div>
  <div class="address-strip">Harbourview Business Suites, 140 Collins Lane, Melbourne Vic 3000</div>
  <div class="web-band">www.<strong>northlensresearch</strong>.com.au</div>
</section>

</body>
</html>
```